Brenwick Homes Realty is seeking to have his informational, lead capture and Internet presence website

white and blue would be prevailed colors with scenarios of Los Angeles icons: Hollywood sign, Santa Monica pier and other beaches with palm trees. It should include information For Buyers, as well as For Sellers; common terminology in the process of purchase and selling houses and basic steps in the process of purchasing and/or selling a house.
Scroll down type of website is prefer, but tabs would be acceptable. Tabs:
About Us. For Buyers. For Sellers, Contact Us.
Links to: Terminology; process of purchase; process of selling.
Updates

Target Market(s)

Mainly focus on BUYERS.

Industry/Entity Type

California Real Estate

Coding

Coded - Design and coding required

Number of Pages Required

3 page

Colors
0054AA
0677BA
7BADD7
CADEEF
E8F1F8

Requirements
Must have
• a slogan under Brenwick Homes Realty: "Southern California Specialists Since 2004". Houses pictures must be Craftman, Country, or Ranch, but no
Nice to have
• On the first page, ABOUT US should be as a map of where to find what visitor needs: For Buyers ( description and link to2nd Page) including at the end description of the process. On 1st page also services offered For Sellers (description of what we do, -3rd page- and at the bottom, process of purchasing). Pages 2 and 3 might need a link to Terminology that will describe used terms. I see my website having at the bottom of every page with my CONTACT US information as well as invitation to send visitor's info to get personalize service. ALSO need as a legal disclaimer licenses numbers and Regulator. (To be provided to winner)
Should not have
• Listings

```html
<!DOCTYPE html>
<html lang="en">
<head>
<meta charset="utf-8">
<title>Brenwick Homes Realty</title>
<link href="https://fonts.googleapis.com/css2?family=Raleway:wght@600;700&family=Roboto:wght@400;500;700&display=swap" rel="stylesheet">
<style>
:root{
  --blue:#0054AA;
  --blue-mid:#0677BA;
  --blue-soft:#7BADD7;
  --blue-pale:#CADEEF;
  --blue-mist:#E8F1F8;
  --ink:#222428;
  --text:#555a60;
  --navy:#0b1a2b;
  --grey-bg:#f6f6f7;
  --white:#ffffff;
}
*{box-sizing:border-box;margin:0;padding:0}
html,body{width:1200px;height:4409px;overflow:hidden}
body{position:relative;font-family:"Roboto",Arial,sans-serif;color:var(--ink);background:var(--white)}
.abs{position:absolute}
h1,h2,h3,.brand-name{font-family:"Raleway",Arial,sans-serif}
section,header,footer{position:absolute;left:0;width:1200px}

/* buttons */
.btn{position:absolute;height:43px;border-radius:22px;background:var(--blue);color:var(--white);
  font:700 15px "Roboto",Arial,sans-serif;display:flex;align-items:center;justify-content:center;gap:8px;
  text-transform:uppercase;letter-spacing:.2px}
.btn svg{width:14px;height:14px}
.btn-light{background:var(--white);color:var(--blue)}

/* header */
.site-header{top:0;height:132px;background:var(--white);border-top:6px solid var(--blue)}
.brand-name{position:absolute;left:111px;top:32px;font-size:32px;font-weight:700;color:#2a2d33;white-space:nowrap}
.brand-slogan{position:absolute;left:128px;top:76px;font-size:14px;color:#3a3d42}
.contact-chip{position:absolute;top:22px;display:flex;gap:12px;align-items:center;white-space:nowrap}
.contact-chip .ico{width:38px;height:38px;border-radius:50%;background:var(--blue);display:flex;align-items:center;justify-content:center;flex:none}
.contact-chip small{display:block;font-size:12px;color:#8a8f96}
.contact-chip strong{display:block;font-size:16px;color:#1d1f22;margin-top:4px}
.main-nav{position:absolute;left:445px;top:82px;width:755px;height:50px;background:var(--blue);
  clip-path:polygon(28px 0,100% 0,100% 100%,0 100%)}
.main-nav ul{list-style:none;display:flex;align-items:center;height:100%;padding-left:64px;color:var(--white);font-size:15px;font-weight:500}
.main-nav li+li::before{content:"|";margin:0 22px}

/* hero */
.hero{top:132px;height:584px;background:linear-gradient(180deg,#7f9bb3 0%,#a9b5ba 30%,#8e8a7a 58%,#5c6a3e 82%,#3f4d2a 100%)}
.hero .shade{position:absolute;inset:0;background:rgba(20,25,30,.28)}
.hero-text{position:absolute;left:0;width:1200px;text-align:center;color:var(--white);font-family:"Raleway",Arial,sans-serif;font-weight:700;white-space:nowrap}
.hero .welcome{top:228px;font-size:36px}
.hero .title{top:265px;font-size:68px}
.hero .slogan{top:350px;font-size:34px}

/* about */
.about{top:716px;height:604px}
.photo{background:linear-gradient(135deg,#8a8f96,#5e6a76 50%,#6b7f4f)}
.about-photo{left:541px;top:87px;width:548px;height:423px;background:linear-gradient(160deg,#8b7a6a 0%,#9aa3ab 35%,#3f6fa3 65%,#5d7f3e 100%)}
.about-card{left:111px;top:114px;width:504px;height:370px;background:var(--white);border-radius:8px;box-shadow:0 10px 40px rgba(0,0,0,.12);padding:34px 39px;z-index:1}
.about-card h2{font-size:40px;font-weight:700;color:#2a2d33}
.about-card h3{font-size:26px;color:var(--blue);margin-top:2px}
.body-copy{font-size:14px;line-height:25.7px;color:var(--text)}
.about-card .body-copy{margin-top:10px;width:410px}

/* blue bands */
.band{background:linear-gradient(180deg,var(--blue) 0%,#0a5aa3 100%);color:var(--white);text-align:center}
.band h2{position:absolute;left:0;width:1200px;font-size:38px;font-weight:700}
.band p{position:absolute;font-size:15px;line-height:25.7px}
.buyers{top:1320px;height:416px}

/* seller services */
.services{top:1736px;height:570px}
.circle-photo{left:151px;top:82px;width:394px;height:394px;border-radius:50%;border:5px solid var(--white);
  box-shadow:0 10px 30px rgba(0,0,0,.2);background:linear-gradient(120deg,#b98a5c 0%,#8a6446 45%,#2f3b5a 70%,#6b5240 100%)}
.services h2{left:604px;top:110px;font-size:40px;line-height:41px;font-weight:700;color:#2a2d33;position:absolute}
.services h3{left:604px;top:206px;font-size:26px;color:var(--blue);position:absolute}
.services .body-copy{left:604px;top:242px;width:468px;position:absolute;font-size:13.5px}

/* sellers */
.sellers{top:2306px;height:514px;background:var(--grey-bg)}
.sellers h2{left:110px;top:77px;font-size:40px;color:#2a2d33;position:absolute}
.sellers .body-copy{left:111px;top:136px;width:470px;position:absolute;font-size:14px}
.accent-block{left:1000px;top:87px;width:99px;height:77px;background:#1e8fd6}
.accent-frame{left:654px;top:351px;width:104px;height:82px;border-left:3px solid var(--blue);border-bottom:3px solid var(--blue);border-radius:0 0 0 8px}
.sellers-photo{left:664px;top:98px;width:425px;height:323px;border:4px solid var(--white);box-shadow:0 6px 20px rgba(0,0,0,.15);
  background:linear-gradient(180deg,#e4e4e2 0%,#cfcdc8 45%,#a98f70 75%,#5c6d8c 100%)}

.terms{top:2820px;height:342px}

/* contact */
.contact{top:3162px;height:519px}
.section-title{position:absolute;left:0;width:1200px;text-align:center;font-size:38px;font-weight:700;color:#2a2d33}
.field{position:absolute;background:var(--white);border-radius:24px;box-shadow:0 4px 18px rgba(0,0,0,.09);
  font-size:13px;color:#8a8f96;padding:0 28px;display:flex;align-items:center}
.field.area{align-items:flex-start;padding-top:22px;border-radius:20px}

/* personalize */
.personal{top:3681px;height:342px;background:var(--blue-mist);text-align:center}
.centered-copy{position:absolute;left:150px;width:900px;text-align:center;font-size:15px;line-height:25.7px;color:#3a3d42}

/* footer */
.site-footer{top:4023px;height:386px;background:var(--navy);color:var(--white)}
.site-footer h4{position:absolute;top:68px;font-size:18px;font-weight:700}
.foot-list{position:absolute;list-style:none;font-size:14px;line-height:34px}
.contact-list li{display:flex;gap:14px;align-items:flex-start;line-height:22px;margin-bottom:14px}
.contact-list svg{width:14px;height:14px;flex:none;margin-top:4px}
.sub-input{position:absolute;left:731px;top:115px;width:236px;height:41px;border-radius:21px;background:var(--white);color:#777;font-size:12px;padding-left:24px;display:flex;align-items:center}
.sub-btn{position:absolute;left:976px;top:115px;width:128px;height:41px;border-radius:21px;background:var(--blue);font-size:15px;font-weight:700;display:flex;align-items:center;justify-content:center}
.social{position:absolute;top:223px;width:31px;height:31px;border-radius:50%;border:1.5px solid var(--white)}
.foot-rule{position:absolute;left:111px;top:317px;width:978px;height:1px;background:rgba(255,255,255,.18)}
.foot-bottom{position:absolute;top:340px;font-size:13px}
</style>
</head>
<body>

<header class="site-header">
  <div class="brand-name">Brenwick Homes Realty</div>
  <div class="brand-slogan">Southern California Specialists Since 2004</div>

  <div class="contact-chip" style="left:670px">
    <div class="ico"><svg width="20" height="16" viewBox="0 0 20 16"><rect x="1" y="1" width="18" height="14" rx="2" fill="none" stroke="#fff" stroke-width="2"/><path d="M2 3l8 6 8-6" fill="none" stroke="#fff" stroke-width="2"/></svg></div>
    <div><small>Email Us:</small><strong>info@brenwick.com</strong></div>
  </div>
  <div class="contact-chip" style="left:892px">
    <div class="ico"><svg width="18" height="18" viewBox="0 0 24 24"><path d="M6.6 10.8a15 15 0 006.6 6.6l2.2-2.2a1 1 0 011-.25 11.4 11.4 0 003.6.57 1 1 0 011 1V20a1 1 0 01-1 1A17 17 0 013 4a1 1 0 011-1h3.5a1 1 0 011 1c0 1.25.2 2.45.57 3.57a1 1 0 01-.25 1z" fill="#fff"/></svg></div>
    <div><small>Call Us Today</small><strong style="font-size:18px">+1 555 010 2040</strong></div>
  </div>

  <nav class="main-nav"><ul><li>Home</li><li>About Us</li><li>For Buyers</li><li>For Sellers</li><li>Contact Us</li></ul></nav>
</header>

<section class="hero">
  <div class="abs" style="inset:0" role="img" aria-label="Photograph of a modern white house with a wooden garage door among trees"></div>
  <div class="shade"></div>
  <div class="hero-text welcome">Welcome to</div>
  <div class="hero-text title">Brenwick Homes Realty</div>
  <div class="hero-text slogan">Southern California Specialists Since 2004</div>
  <div class="btn" style="left:510px;top:424px;width:180px">Get Started <svg viewBox="0 0 14 14"><circle cx="7" cy="7" r="7" fill="#fff"/><path d="M5.5 4l3 3-3 3" fill="none" stroke="#0054AA" stroke-width="2"/></svg></div>
</section>

<section class="about">
  <div class="abs about-photo" role="img" aria-label="Photograph of a smiling family standing in front of their house"></div>
  <div class="abs about-card">
    <h2>About Us</h2>
    <h3>For Buyers</h3>
    <p class="body-copy">Lorem ipsum dolor sit amet, consectetur adipiscing elit, sed do eiusmod tempor incididunt ut labore et dolore magna aliqua. Ut enim ad minim veniam, quis nostrud exercitation ullamco laboris nisi ut aliquip ex ea commodo consequat. Duis aute irure dolor in reprehenderit in voluptate velit esse cillum dolore eu fugiat nulla Excepteur sint occaecat cupidatat non proident.</p>
    <div class="btn" style="left:39px;top:286px;width:168px">Learn More <svg viewBox="0 0 14 14"><circle cx="7" cy="7" r="7" fill="#fff"/><path d="M5.5 4l3 3-3 3" fill="none" stroke="#0054AA" stroke-width="2"/></svg></div>
  </div>
</section>

<section class="band buyers">
  <h2 style="top:72px">For Buyers</h2>
  <p style="left:150px;top:136px;width:900px">Lorem ipsum dolor sit amet, consectetur adipiscing elit, sed do eiusmod tempor incididunt ut labore et dolore magna aliqua. Ut enim ad minim veniam, quis nostrud exercitation ullamco laboris nisi ut aliquip ex ea commodo consequat. Duis aute irure dolor in reprehenderit in voluptate velit esse cillum dolore eu fugiat nulla pariatur.Lorem ipsum dolor sit amet, consectetur adipiscing elit, sed do eiusmod tempor incididunt ut labore et dolore magna aliqua. Ut enim ad minim veniam, quis nostrud exercitation ullamco laboris nisi ut aliquip ex ea commodo consequat. Duis aute irure dolor in reprehenderit .</p>
  <div class="btn btn-light" style="left:515px;top:296px;width:168px">Learn More <svg viewBox="0 0 14 14"><circle cx="7" cy="7" r="7" fill="#0054AA"/><path d="M5.5 4l3 3-3 3" fill="none" stroke="#fff" stroke-width="2"/></svg></div>
</section>

<section class="services">
  <div class="abs circle-photo" role="img" aria-label="Photograph of a craftsman building a wooden chair in a workshop"></div>
  <h2>Services offered For<br>Sellers</h2>
  <h3>What We do</h3>
  <p class="body-copy">Lorem ipsum dolor sit amet, consectetur adipiscing elit, sed do eiusmod tempor incididunt ut labore et dolore magna aliqua. Ut enim ad minim veniam, quis nostrud exercitation ullamco laboris nisi ut aliquip ex ea commodo consequat. Duis aute irure dolor in reprehenderit in voluptate velit esse cillum dolore eu fugiat nulla Excepteur sint occaecat cupidatat non proident. reprehenderit in voluptate velit esse cillum dolore</p>
  <div class="btn" style="left:604px;top:406px;width:168px">Learn More <svg viewBox="0 0 14 14"><circle cx="7" cy="7" r="7" fill="#fff"/><path d="M5.5 4l3 3-3 3" fill="none" stroke="#0054AA" stroke-width="2"/></svg></div>
</section>

<section class="sellers">
  <h2>For Sellers</h2>
  <p class="body-copy">Lorem ipsum dolor sit amet, consectetur adipiscing elit, sed do eiusmod tempor incididunt ut labore et dolore magna aliqua. Ut enim ad minim veniam, quis nostrud exercitation ullamco laboris nisi ut aliquip ex ea commodo consequat. Duis aute irure dolor in reprehenderit in voluptate velit esse cillum dolore eu fugiat nulla Excepteur sint occaecat cupidatat non proident. reprehenderit in voluptate velit esse cillum dolore eu fugiat nulla Excepteur sint occaecat cupida sunt in culpa qui officia deserunt mollit anim id est laborumx cepteur sint occaecat cupidatat non proident, sunt in culpa qui officia deserunt mollit anim id est laborum.</p>
  <div class="btn" style="left:111px;top:392px;width:168px">Learn More <svg viewBox="0 0 14 14"><circle cx="7" cy="7" r="7" fill="#fff"/><path d="M5.5 4l3 3-3 3" fill="none" stroke="#0054AA" stroke-width="2"/></svg></div>
  <div class="abs accent-block"></div>
  <div class="abs accent-frame"></div>
  <div class="abs sellers-photo" role="img" aria-label="Photograph of a real estate agent showing a kitchen to a couple"></div>
</section>

<section class="band terms">
  <h2 style="top:62px">Terminology</h2>
  <p style="left:160px;top:134px;width:880px">Lorem ipsum dolor sit amet, consectetur adipiscing elit, sed do eiusmod tempor incididunt ut labore et dolore magna aliqua. Ut enim ad minim veniam, quis nostrud exercitation ullamco laboris nisi ut aliquip ex ea commodo consequat. Duis aute irure dolor in reprehenderit in voluptate velit esse cillum dolore eu fugiat nulla pariatur.</p>
  <div class="btn btn-light" style="left:515px;top:232px;width:168px">Learn More <svg viewBox="0 0 14 14"><circle cx="7" cy="7" r="7" fill="#0054AA"/><path d="M5.5 4l3 3-3 3" fill="none" stroke="#fff" stroke-width="2"/></svg></div>
</section>

<section class="contact">
  <h2 class="section-title" style="top:78px">Contact Us</h2>
  <div class="field" style="left:195px;top:154px;width:390px;height:48px">Name</div>
  <div class="field" style="left:195px;top:219px;width:390px;height:48px">Email Address</div>
  <div class="field" style="left:195px;top:284px;width:390px;height:48px">Phone Number</div>
  <div class="field area" style="left:609px;top:151px;width:396px;height:185px">Message</div>
  <div class="btn" style="left:512px;top:380px;width:176px">Submit Now <svg viewBox="0 0 14 14"><circle cx="7" cy="7" r="7" fill="#fff"/><path d="M5.5 4l3 3-3 3" fill="none" stroke="#0054AA" stroke-width="2"/></svg></div>
</section>

<section class="personal">
  <h2 class="section-title" style="top:66px">Get Personalize Service</h2>
  <p class="centered-copy" style="top:128px">Lorem ipsum dolor sit amet, consectetur adipiscing elit, sed do eiusmod tempor incididunt ut labore et dolore magna aliqua. Ut enim ad minim veniam, quis nostrud exercitation ullamco laboris nisi ut aliquip ex ea commodo consequat. Duis aute irure dolor in reprehenderit in voluptate velit esse cillum dolore eu fugiat nulla pariatur.</p>
  <div class="btn" style="left:516px;top:236px;width:168px">Contact Us <svg viewBox="0 0 14 14"><circle cx="7" cy="7" r="7" fill="#fff"/><path d="M5.5 4l3 3-3 3" fill="none" stroke="#0054AA" stroke-width="2"/></svg></div>
</section>

<footer class="site-footer">
  <h4 style="left:94px">Contact Us</h4>
  <ul class="foot-list contact-list" style="left:94px;top:114px;width:240px">
    <li><svg viewBox="0 0 14 14"><path d="M7 1a4.5 4.5 0 00-4.5 4.5C2.5 9 7 13 7 13s4.5-4 4.5-7.5A4.5 4.5 0 007 1z" fill="#fff"/><circle cx="7" cy="5.5" r="1.6" fill="#0b1a2b"/></svg><span>7575,Lorem ipsum dolor sit sectetur adipiscing elit 48114</span></li>
    <li><svg viewBox="0 0 14 14"><rect x="1" y="2.5" width="12" height="9" rx="1" fill="#fff"/><path d="M1.5 3.5L7 8l5.5-4.5" fill="none" stroke="#0b1a2b" stroke-width="1.2"/></svg><span>info@brenwickhomesrealty.com</span></li>
    <li><svg viewBox="0 0 24 24"><path d="M6.6 10.8a15 15 0 006.6 6.6l2.2-2.2a1 1 0 011-.25 11.4 11.4 0 003.6.57 1 1 0 011 1V20a1 1 0 01-1 1A17 17 0 013 4a1 1 0 011-1h3.5a1 1 0 011 1c0 1.25.2 2.45.57 3.57a1 1 0 01-.25 1z" fill="#fff"/></svg><span>+1 555 010 2040</span></li>
    <li><svg viewBox="0 0 14 14"><rect x="1" y="5" width="12" height="7" rx="1" fill="#fff"/><rect x="3.5" y="1.5" width="7" height="4" fill="none" stroke="#fff" stroke-width="1.3"/><rect x="4" y="8" width="6" height="1.2" fill="#0b1a2b"/></svg><span>555 010 2041</span></li>
  </ul>

  <h4 style="left:377px">Quick&nbsp; Links</h4>
  <ul class="foot-list" style="left:377px;top:104px">
    <li>legal</li><li>Terminology</li><li>Disclaimer</li><li>Process of purchase</li><li>Process of selling</li>
  </ul>

  <h4 style="left:582px">Navbar</h4>
  <ul class="foot-list" style="left:583px;top:104px">
    <li>Home</li><li>About Us</li><li>For Buyers</li><li>For Sellers</li><li>Contact Us</li>
  </ul>

  <h4 style="left:728px">Subscribe for Updates</h4>
  <div class="sub-input">Emaill Address</div>
  <div class="sub-btn">SUBMIT</div>
  <div class="abs" style="left:728px;top:205px;font-size:13px;font-weight:700;display:flex;gap:10px;align-items:center">
    <svg width="13" height="13" viewBox="0 0 14 14"><rect x="1" y="2" width="10" height="10" rx="1.5" fill="none" stroke="#fff" stroke-width="1.4"/><path d="M4 7l2.3 2.3L13 2.5" fill="none" stroke="#fff" stroke-width="1.6"/></svg>
    Yes, Please Contact me.
  </div>
  <div class="social" style="left:728px"></div>
  <div class="social" style="left:771px"></div>
  <div class="social" style="left:814px"></div>

  <div class="foot-rule"></div>
  <div class="foot-bottom" style="left:111px">Licenses Numbers:12345678</div>
  <div class="foot-bottom" style="left:765px">© 2023&nbsp; Brenwick Homes Realty |&nbsp; All Rights Reserved&nbsp; |</div>
</footer>

</body>
</html>
```